Pelkman Agency (http://pa.quorvexstudio.com/)

We are looking for a similar design to what we have, but more professional looking and cleaned up with links and logo that is not so grainy looking. We are an independent insurance agency marketing to personal and commercial clients. We offer all commercial lines markets and all personal lines. We target excavators, landscapers, restaurants, golf courses, contractors. Please look at http://pa.quorvexstudio.com/ which we had designed but do not like it, it will give you an idea of what we are looking for.

Target Market(s)

Commercial and personal insurance. All business products and all personal (homeowners, auto, antique auto, umbrella)

Industry/Entity Type

It Professional

Logo Text

Knowledge Building Your Assurance

Number of Pages Required

5+ page

Colors
000000
848484
0255a3

```html
<!DOCTYPE html>
<html lang="en">
<head>
<meta charset="utf-8">
<title>Pelkman Agency</title>
<link rel="stylesheet" href="https://fonts.googleapis.com/css2?family=Open+Sans:wght@400;600;700;800&display=swap">
<style>
:root{
  --ink:#1f1f1f;
  --grey:#848484;
  --text:#555555;
  --blue:#0255a3;
  --blue-deep:#0a3d8f;
  --navy:#0c2f6e;
  --band-top:#0d55c2;
  --band-bottom:#0a3c8c;
  --footer:#252525;
  --white:#ffffff;
}
*{box-sizing:border-box;margin:0;padding:0}
html,body{width:1068px;height:1200px;overflow:hidden;background:var(--white);font-family:"Open Sans",Arial,sans-serif}
.page{position:relative;width:1068px;height:1200px}

/* header */
.site-header{position:absolute;left:0;top:0;width:1068px;height:122px;background:var(--white)}
.brand{position:absolute;left:88px;top:72px;display:flex;align-items:center;gap:10px}
.brand-mark{width:26px;height:26px;background:var(--ink)}
.brand-name{font-size:19px;font-weight:600;color:var(--blue);letter-spacing:.5px}
.search{position:absolute;left:820px;top:28px;width:160px;height:36px;background:#f3f3f3;border-radius:2px}
.search svg{position:absolute;left:10px;top:11px}
.main-nav{position:absolute;top:84px;left:0;width:1068px;height:38px}
.main-nav a{position:absolute;top:0;font-size:13.5px;color:#666;text-decoration:none;white-space:nowrap}
.main-nav a.active{color:var(--blue)}
.main-nav a.active::after{content:"";position:absolute;left:0;right:0;top:36px;height:3px;background:var(--blue)}

/* hero */
.hero{position:absolute;left:0;top:122px;width:1068px;height:392px;
  background:linear-gradient(90deg,#4a6a90 0%,#6f8db0 30%,#5a7596 55%,#3d4a5a 75%,#2f3640 100%)}
.hero-photo{position:absolute;inset:0;background:radial-gradient(ellipse at 25% 40%,rgba(220,228,238,.55),transparent 55%)}
.hero-copy{position:absolute;left:86px;top:150px;color:var(--white);text-shadow:0 1px 3px rgba(0,0,0,.4)}
.hero-title{font-size:37px;font-weight:800;letter-spacing:.5px;line-height:1}
.hero-sub{margin-top:10px;font-size:22px;font-weight:400;line-height:27px;letter-spacing:-.3px}
.hero-note{margin-top:12px;font-size:10px;line-height:12.5px}
.slide-arrow{position:absolute;top:188px;width:40px;height:40px;border-radius:50%}
.slide-prev{left:25px;background:rgba(40,40,40,.8)}
.slide-next{left:975px}
.slide-arrow svg{position:absolute;left:13px;top:11px}

/* service band */
.services{position:absolute;left:0;top:514px;width:1068px;height:264px;background:linear-gradient(180deg,var(--band-top),var(--band-bottom))}
.service{position:absolute;top:-58px;width:220px;text-align:center;color:var(--white)}
.service-icon{width:110px;height:110px;margin:0 auto;border-radius:50%;border:3px solid var(--white);background:var(--blue-deep);display:flex;align-items:center;justify-content:center;box-shadow:0 8px 8px -6px rgba(0,0,0,.35)}
.service h3{margin-top:26px;font-size:14.5px;font-weight:600;letter-spacing:.3px}
.service p{margin-top:12px;font-size:11.5px;line-height:18.5px;color:#e4ecf8}
.btn{display:inline-block;margin-top:16px;width:95px;height:36px;line-height:36px;background:var(--navy);color:var(--white);font-size:13px;border-radius:2px;text-decoration:none}

/* business area */
.area-title{position:absolute;left:0;top:806px;width:1068px;text-align:center;font-size:28px;font-weight:700;color:var(--ink)}
.area{position:absolute;top:870px;width:175px}
.area-photo{width:175px;height:111px}
.area h4{margin-top:20px;font-size:19px;font-weight:700;color:var(--blue)}
.area p{margin-top:10px;font-size:11.5px;line-height:18.5px;color:var(--text)}

/* footer */
.site-footer{position:absolute;left:0;top:1122px;width:1068px;height:78px;background:var(--footer)}
.footer-nav{position:absolute;left:88px;top:20px;font-size:11.5px;color:#bbb;white-space:nowrap}
.footer-nav a{color:#ccc;text-decoration:none}
.footer-nav span{margin:0 10px}
.copyright{position:absolute;left:88px;top:44px;font-size:10px;color:#aaa}
.social{position:absolute;left:916px;top:22px;display:flex;gap:7px}
.social span{width:17px;height:17px;border-radius:2px}
</style>
</head>
<body>
<div class="page">

  <header class="site-header">
    <div class="brand"><span class="brand-mark"></span><span class="brand-name">PELKMAN AGENCY</span></div>
    <div class="search">
      <svg width="13" height="13" viewBox="0 0 13 13"><circle cx="5.5" cy="5.5" r="4" fill="none" stroke="#333" stroke-width="2"/><line x1="8.5" y1="8.5" x2="12" y2="12" stroke="#333" stroke-width="2.2"/></svg>
    </div>
    <nav class="main-nav">
      <a class="active" href="#" style="left:378px">Home</a>
      <a href="#" style="left:451px">Personal Insurance</a>
      <a href="#" style="left:589px">Business Insurance</a>
      <a href="#" style="left:726px">Service Center</a>
      <a href="#" style="left:836px">About Us</a>
      <a href="#" style="left:918px">Contact Us</a>
    </nav>
  </header>

  <section class="hero">
    <div class="hero-photo" role="img" aria-label="Photo of a climber scaling a rock face above clouds and a distant mountain"></div>
    <div class="hero-copy">
      <h1 class="hero-title">LIFE INSURANCE</h1>
      <p class="hero-sub">SMALL ENOUGH TO CARE, BIG ENOUGH<br>TO MAKE A DIFFERENCE</p>
      <p class="hero-note">Please find information about our agency, its principles ,<br>and the various types of insurance coverages that we provide.</p>
    </div>
    <a class="slide-arrow slide-prev" href="#" aria-label="Previous slide"><svg width="12" height="18" viewBox="0 0 12 18"><path d="M9 2 3 9l6 7" fill="none" stroke="#fff" stroke-width="3"/></svg></a>
    <a class="slide-arrow slide-next" href="#" aria-label="Next slide"><svg width="12" height="18" viewBox="0 0 12 18"><path d="M3 2l6 7-6 7" fill="none" stroke="#ddd" stroke-width="2.5"/></svg></a>
  </section>

  <section class="services">
    <div class="service" style="left:77px">
      <div class="service-icon"><svg width="38" height="32" viewBox="0 0 38 32"><rect x="12" y="1" width="14" height="7" rx="2" fill="none" stroke="#fff" stroke-width="3"/><rect x="1" y="7" width="36" height="24" rx="3" fill="#fff"/><rect x="8" y="7" width="2.5" height="24" fill="#0a3d8f"/><rect x="27.5" y="7" width="2.5" height="24" fill="#0a3d8f"/></svg></div>
      <h3>BUSINESS INSURANCE</h3>
      <p>Neque porro quisquam est qui dolorem ipsum quia dolor sit amet, consectetur, adipisci velit...</p>
      <a class="btn" href="#">Read More</a>
    </div>
    <div class="service" style="left:306px">
      <div class="service-icon"><svg width="42" height="34" viewBox="0 0 42 34"><path d="M8 14 12 4h18l4 10h4v14h-5v5h-6v-5H15v5H9v-5H4V14z" fill="#fff"/><path d="M13 13 15.5 7h11l2.5 6z" fill="#0a3d8f"/><circle cx="10" cy="21" r="3" fill="#0a3d8f"/><circle cx="32" cy="21" r="3" fill="#0a3d8f"/></svg></div>
      <h3>AUTO INSURANCE</h3>
      <p>Neque porro quisquam est qui dolorem ipsum quia dolor sit amet, consectetur, adipisci velit...</p>
      <a class="btn" href="#">Read More</a>
    </div>
    <div class="service" style="left:543px">
      <div class="service-icon"><svg width="38" height="34" viewBox="0 0 38 34"><path d="M19 33 4 18C-2 12 2 1 10 1c4 0 7 2 9 5 2-3 5-5 9-5 8 0 12 11 6 17z" fill="#fff"/></svg></div>
      <h3>LIFE INSURANCE</h3>
      <p>Neque porro quisquam est qui dolorem ipsum quia dolor sit amet, consectetur, adipisci velit...</p>
      <a class="btn" href="#">Read More</a>
    </div>
    <div class="service" style="left:772px">
      <div class="service-icon"><svg width="34" height="30" viewBox="0 0 34 30"><path d="M17 1 1 15h4l12-10 12 10h4z" fill="#fff"/><rect x="24" y="2" width="4" height="7" fill="#fff"/><path d="M7 16 17 8l10 8v13h-7v-8h-6v8H7z" fill="#fff"/></svg></div>
      <h3>HOME INSURANCE</h3>
      <p>Neque porro quisquam est qui dolorem ipsum quia dolor sit amet, consectetur, adipisci velit...</p>
      <a class="btn" href="#">Read More</a>
    </div>
  </section>

  <h2 class="area-title">OUR BUSINESS AREA</h2>

  <article class="area" style="left:88px">
    <div class="area-photo" role="img" aria-label="Photo of an orange excavator on a dirt site at dusk" style="background:linear-gradient(180deg,#2d4f86,#6b7a8c 55%,#7a6450)"></div>
    <h4>EXCAVATORS</h4>
    <p>Lorem ipsum dolor sit amet, con-sectetur adipiscing elit, sed do eiusmod</p>
  </article>
  <article class="area" style="left:268px">
    <div class="area-photo" role="img" aria-label="Photo of a landscaped lawn with flower beds" style="background:linear-gradient(180deg,#3f5a2a,#5f9a2e 55%,#7cc043)"></div>
    <h4>LANDSCAPERS</h4>
    <p>Lorem ipsum dolor sit amet, con-sectetur adipiscing elit, sed do eiusmod</p>
  </article>
  <article class="area" style="left:447px">
    <div class="area-photo" role="img" aria-label="Photo of a warmly lit restaurant table setting" style="background:linear-gradient(180deg,#3a2010,#8a5424 55%,#c8884a)"></div>
    <h4>RESTAURANTS</h4>
    <p>Lorem ipsum dolor sit amet, con-sectetur adipiscing elit, sed do eiusmod</p>
  </article>
  <article class="area" style="left:626px">
    <div class="area-photo" role="img" aria-label="Photo of a golfer mid-swing on a course under a dramatic sky" style="background:linear-gradient(180deg,#3a4150,#8a8f8a 55%,#3f6a2a)"></div>
    <h4>GOLF COURSES</h4>
    <p>Lorem ipsum dolor sit amet, con-sectetur adipiscing elit, sed do eiusmod</p>
  </article>
  <article class="area" style="left:805px">
    <div class="area-photo" role="img" aria-label="Photo of a construction worker in a yellow hard hat carrying lumber" style="background:linear-gradient(180deg,#6f9ad0,#b9a27a 55%,#2a3550)"></div>
    <h4>CONTRACTOR</h4>
    <p>Lorem ipsum dolor sit amet, con-sectetur adipiscing elit, sed do eiusmod</p>
  </article>

  <footer class="site-footer">
    <nav class="footer-nav">
      <a href="#">Home</a><span>|</span><a href="#">Personal Insurance</a><span>|</span><a href="#">Business Insurance</a><span>|</span><a href="#">Service Center</a><span>|</span><a href="#">About Us</a><span>|</span><a href="#">Contact Us</a>
    </nav>
    <p class="copyright">© 2015 Pelkman Agency. All rights reserved.</p>
    <div class="social" aria-label="Social links">
      <span style="background:#3b5ea8"></span>
      <span style="background:#3fa9d6"></span>
      <span style="background:#e8731e"></span>
    </div>
  </footer>

</div>
</body>
</html>
```